ADA COMPLIANCE

We are in need of flyer or tri fold page for ada compliance, handicap ramps and parking lot striping.

Target Market(s)

Commercial Construction Industry

Industry/Entity Type

Parking

Font styles to use
Other font styles liked:
• Felix Titling

Colors
0355a3
acd036

Requirements
Must have
• Our Company Name and logo, 8004172593 number License #2837406
• List of services provided in uploaded images. Navy blue with high vizability green

```html
<!DOCTYPE html>
<html lang="en">
<head>
<meta charset="utf-8">
<title>Paragon Site Services – ADA Compliance Tri-fold</title>
<link href="https://fonts.googleapis.com/css2?family=Cinzel:wght@400;600&family=Open+Sans:wght@400;600&display=swap" rel="stylesheet">
<style>
  :root{
    --navy:#0355a3;
    --green:#acd036;
    --paper:#f4f5f5;
    --ink:#2b2b2b;
    --stage:#e4e4e4;
    --asphalt:#3a4149;
  }
  *{margin:0;padding:0;box-sizing:border-box}
  html,body{width:1200px;height:800px;overflow:hidden;background:var(--stage)}
  body{position:relative;font-family:"Open Sans",Arial,sans-serif;color:var(--ink)}
  .sheet{position:absolute;top:180px;width:570px;height:440px;background:var(--paper);box-shadow:0 6px 18px rgba(0,0,0,.18);overflow:hidden}
  .sheet--inside{left:20px}
  .sheet--outside{left:610px}
  .sheet svg.art{position:absolute;inset:0}
  .heading{font-family:"Cinzel",Georgia,serif;color:var(--navy);font-weight:400;letter-spacing:.5px}
  .inside-copy{position:absolute;left:208px;top:58px;width:165px}
  .inside-copy .heading{font-size:13px;margin-bottom:4px}
  .lead{font-size:9.5px;font-weight:600;margin-bottom:3px}
  .service-list{list-style:none;font-size:9.5px;line-height:14px}
  .service-list li{padding-left:10px;position:relative}
  .service-list li::before{content:"";position:absolute;left:0;top:4px;border-left:6px solid var(--navy);border-top:3.5px solid transparent;border-bottom:3.5px solid transparent}
  .rule{height:1px;background:linear-gradient(90deg,var(--navy),var(--green));margin:14px 0 12px}
  .band-text{position:absolute;left:205px;top:414px;font-family:"Cinzel",Georgia,serif;font-size:10px;color:#fff;letter-spacing:.5px}
  .about{position:absolute;left:14px;top:40px;width:162px;color:#fff}
  .about .heading{font-size:14px;margin-bottom:8px}
  .about p{font-size:7.4px;line-height:10.4px;margin-bottom:7px;text-align:justify}
  .contact{position:absolute;left:200px;top:355px;width:170px;text-align:center;color:#fff;font-family:"Cinzel",Georgia,serif;font-size:9.5px;line-height:14px;letter-spacing:.4px}
  .brand{position:absolute;left:400px;top:88px;width:160px;display:flex;align-items:center;gap:6px;color:var(--navy)}
  .brand-mark{width:16px;height:16px;border-radius:50%;background:var(--navy);flex:none}
  .brand-name{font-family:"Cinzel",Georgia,serif;font-size:13px;line-height:14px}
  .brand-name small{display:block;font-size:7px;letter-spacing:.6px}
  .tagline{position:absolute;left:452px;top:392px;width:112px;font-family:"Cinzel",Georgia,serif;font-size:10.5px;color:var(--navy);line-height:12px;white-space:nowrap}
</style>
</head>
<body>

<section class="sheet sheet--inside" aria-label="Brochure inside spread">
  <svg class="art" width="570" height="440" viewBox="0 0 570 440">
    <defs>
      <linearGradient id="lotPhoto" x1="0" y1="0" x2="0" y2="1">
        <stop offset="0" stop-color="#c9b04a"/><stop offset=".3" stop-color="#6f7f93"/><stop offset="1" stop-color="#3c4148"/>
      </linearGradient>
      <linearGradient id="stallPhoto" x1="0" y1="0" x2="1" y2="1">
        <stop offset="0" stop-color="#5b6670"/><stop offset=".6" stop-color="#2f3a47"/><stop offset="1" stop-color="#1f5fa6"/>
      </linearGradient>
    </defs>
    <rect class="photo" role="img" aria-label="Photo of a freshly striped parking lot beside an event tent" x="0" y="0" width="190" height="440" fill="url(#lotPhoto)"/>
    <polygon fill="var(--green)" points="190,0 270,0 190,85"/>
    <rect class="photo" role="img" aria-label="Photo of an accessible parking area" x="456" y="0" width="114" height="112" fill="#6b7580"/>
    <rect x="388" y="8" width="62" height="62" fill="var(--navy)"/>
    <g fill="#fff" transform="translate(402,16)">
      <circle cx="14" cy="5" r="4.5"/>
      <path d="M11 12h6v12h12l6 14-4 1.6-5-11.6H11z"/>
      <path d="M8 20a12 12 0 1 0 17 16l-2-3a8.5 8.5 0 1 1-13-10z"/>
    </g>
    <polygon fill="var(--green)" points="380,150 570,118 570,205"/>
    <polygon class="photo" role="img" aria-label="Photo of blue accessible parking stalls with painted symbols" fill="url(#stallPhoto)" points="380,212 570,180 570,332 380,402"/>
    <polygon fill="var(--navy)" points="190,405 380,400 570,330 570,440 190,440"/>
  </svg>

  <div class="inside-copy">
    <h2 class="heading">What exactly is it?</h2>
    <p class="lead">The application of traffic pain to:</p>
    <ul class="service-list">
      <li>Parking Lot Lines</li>
      <li>Curbing</li>
      <li>Handicap Logos</li>
      <li>Fire Lanes &amp; No Parking Zone</li>
      <li>Pretty much any makings on a parking lot area</li>
    </ul>
    <div class="rule"></div>
    <h2 class="heading">Parking Lot Striping</h2>
    <ul class="service-list">
      <li>Line Striping &amp; Stenciling</li>
      <li>Handicap ADA Striping</li>
      <li>Curb Painting</li>
      <li>Sign &amp; Poles</li>
      <li>Car Stop &amp; Bollards</li>
      <li>Game Court</li>
      <li>Raised Pavement Markers</li>
      <li>Thermoplastic</li>
      <li>Pallet Striping</li>
    </ul>
  </div>
  <p class="band-text">WWW.PARAGONSITE.COM | 800-417-2593</p>
</section>

<section class="sheet sheet--outside" aria-label="Brochure outside spread">
  <svg class="art" width="570" height="440" viewBox="0 0 570 440">
    <defs>
      <linearGradient id="buildPhoto" x1="0" y1="0" x2="1" y2="1">
        <stop offset="0" stop-color="#b9a48c"/><stop offset="1" stop-color="#6d7378"/>
      </linearGradient>
      <linearGradient id="lotPhoto2" x1="0" y1="0" x2="1" y2="1">
        <stop offset="0" stop-color="#c9a89a"/><stop offset=".45" stop-color="#3b4551"/><stop offset="1" stop-color="#2a5f9c"/>
      </linearGradient>
    </defs>
    <rect x="0" y="0" width="190" height="440" fill="var(--green)"/>
    <polygon class="photo" role="img" aria-label="Photo of a building entrance with an accessible ramp and railings" fill="url(#buildPhoto)" points="0,350 190,305 190,440 0,440"/>
    <rect x="190" y="0" width="8" height="300" fill="var(--green)"/>
    <g fill="var(--navy)" transform="translate(205,270) scale(.85)">
      <circle cx="14" cy="5" r="4.5"/>
      <path d="M11 12h6v12h12l6 14-4 1.6-5-11.6H11z"/>
      <path d="M8 20a12 12 0 1 0 17 16l-2-3a8.5 8.5 0 1 1-13-10z"/>
    </g>
    <path fill="var(--navy)" d="M190 330 Q300 318 380 250 L380 440 L190 440Z"/>
    <polygon class="photo" role="img" aria-label="Photo of a striped parking lot from above" fill="#7d8a84" points="380,0 570,0 570,70 380,40"/>
    <polygon fill="var(--navy)" points="505,150 570,112 570,200"/>
    <polygon class="photo" role="img" aria-label="Photo of accessible parking stalls in front of a post office" fill="url(#lotPhoto2)" points="380,175 570,190 570,325 380,365"/>
    <polygon fill="var(--navy)" points="380,365 440,352 440,440 380,440"/>
    <polygon fill="var(--green)" points="440,352 570,325 570,440 440,440"/>
  </svg>

  <div class="about">
    <h2 class="heading">About Us</h2>
    <p>Paragon Site Services, Inc. is a full-service, architecture, engineering, interior design, turnkey property management, design-build and construction firm that delivers clients around California the highest quality solutions on time, on budget and above and beyond expectations.</p>
    <p>Founded in 2012, we partner with our clients, consultants, suppliers, subcontractors and communities to deliver building solutions of the highest standard.</p>
    <p>Paragon Site Services, Inc. has dramatically set new standards for design, quality and craftsmanship, efficient project management, cost containment and worker safety. We've integrated the building process from head to tail and adopted new technologies that bring state of the art design-build opportunities to clients and their communities.</p>
  </div>

  <div class="contact">
    800-417-2593<br>
    WWW.PARAGONSITE.COM<br>
    INFO@PARAGONSITE.COM
  </div>

  <div class="brand">
    <span class="brand-mark"></span>
    <span class="brand-name">PARAGON<small>SITE SERVICES INC.</small></span>
  </div>

  <p class="tagline">ADA Compliance<br>Experts</p>
</section>

</body>
</html>
```